Unique Construction Safety Sign Needed

We are in need of a 4ft by 4ft sign that outlines the required personal protective equipment needed on our jobsite. The sign should feature a construction figure with call outs to what they are wearing. Ideally we'd like to see 2 options one with a male construction figure and one with a female construction figure.

Industry/Entity Type

Construction Company

Font styles to use
Sans Serif

Colors

Designer to choose colors to be used in the design.

Requirements
Must have
• The Bluetide secure logo and Marlowe logo prominently featured. Please showcase 2 genders if possible. either side by side on one sign or 1 sign of each. Callouts to each item of PPE needed: Hard hat, eye protection, high visibility vest, work shirt, hearing protection, pants or overalls, gloves, work boots,
Nice to have
• We love the hollis construction sign attached in the examples. something similar to this style would be a HOMERUN.
Should not have
• anything that looks too cartoon. We want this to be taken seriously on the jobsite as safety is important.

```html
<!DOCTYPE html>
<html lang="en">
<head>
<meta charset="utf-8">
<title>Jobsite PPE Requirements – Bluetide secure</title>
<link href="https://fonts.googleapis.com/css2?family=Roboto:wght@700;900&display=swap" rel="stylesheet">
<style>
  :root {
    --accent: #e8562a;
    --ink: #1a1a1a;
    --sky-top: #d9e5eb;
    --sky-bottom: #fbfcfd;
    --figure-hat: #f6d43a;
    --figure-vest: #f07d22;
    --figure-shirt: #1f6fc0;
    --figure-pants: #8a6643;
  }
  html, body {
    margin: 0;
    padding: 0;
    width: 1200px;
    height: 1200px;
    overflow: hidden;
    background: var(--sky-bottom);
  }
  .sign {
    position: relative;
    width: 1200px;
    height: 1200px;
    background: linear-gradient(180deg, var(--sky-top) 0%, #e6eef2 45%, var(--sky-bottom) 80%);
    font-family: "Roboto", Arial, sans-serif;
  }
  .worker-figure {
    position: absolute;
    left: 408px;
    top: 53px;
    width: 386px;
    height: 1089px;
    border-radius: 150px 150px 60px 60px;
    background: linear-gradient(180deg,
      var(--figure-hat) 0%, var(--figure-hat) 11%,
      #efc9a6 11%, #efc9a6 22%,
      var(--figure-vest) 22%, var(--figure-shirt) 30%, var(--figure-vest) 40%, var(--figure-vest) 55%,
      var(--figure-pants) 55%, var(--figure-pants) 92%,
      #b9a57a 92%, #a8956c 100%);
    opacity: 0.9;
  }
  .callout-lines {
    position: absolute;
    inset: 0;
  }
  .ppe-item {
    position: absolute;
    width: 360px;
    text-align: center;
  }
  .ppe-icon {
    display: block;
    margin: 0 auto;
    width: 120px;
    height: 120px;
  }
  .ppe-label {
    display: block;
    margin-top: 10px;
    color: var(--accent);
    font-weight: 700;
    font-size: 21px;
    letter-spacing: 0.2px;
    white-space: nowrap;
  }
  .brand {
    position: absolute;
    left: 818px;
    top: 1040px;
    width: 330px;
    text-align: right;
    color: var(--ink);
    font-weight: 900;
  }
  .brand-name {
    display: block;
    font-size: 44px;
    line-height: 1;
  }
  .brand-sub {
    display: block;
    margin-top: 10px;
    font-size: 18px;
  }
</style>
</head>
<body>
<main class="sign">

  <div class="worker-figure" role="img" aria-label="Illustration of a construction worker wearing a yellow hard hat, safety goggles, ear muffs, blue work shirt, orange high visibility vest with fall harness, gloves, brown work pants and tan work boots"></div>

  <svg class="callout-lines" width="1200" height="1200" viewBox="0 0 1200 1200" aria-hidden="true">
    <g fill="none" stroke="#111" stroke-width="2">
      <polyline points="327,98 527,98"/>
      <polyline points="850,113 678,113 637,156"/>
      <polyline points="327,383 405,383 405,184 518,184"/>
      <polyline points="850,469 638,469"/>
      <polyline points="850,659 801,659"/>
      <polyline points="850,852 764,852 680,706 633,706"/>
      <polyline points="323,702 361,759 494,759"/>
      <polyline points="326,949 421,1067 479,1067"/>
    </g>
    <g fill="#111">
      <circle cx="527" cy="98" r="5"/>
      <circle cx="637" cy="156" r="5"/>
      <circle cx="518" cy="184" r="5"/>
      <circle cx="638" cy="469" r="5"/>
      <circle cx="801" cy="659" r="5"/>
      <circle cx="633" cy="706" r="5"/>
      <circle cx="494" cy="759" r="5"/>
      <circle cx="479" cy="1067" r="5"/>
    </g>
  </svg>

  <!-- Left column -->
  <div class="ppe-item" style="left:65px; top:35px;">
    <svg class="ppe-icon" viewBox="0 0 120 120" aria-hidden="true">
      <circle cx="60" cy="60" r="57" fill="none" stroke="var(--accent)" stroke-width="3"/>
      <path d="M26 74 Q26 36 60 34 Q94 36 94 74 Z" fill="var(--accent)"/>
      <rect x="20" y="74" width="80" height="8" rx="3" fill="var(--accent)"/>
    </svg>
    <span class="ppe-label">HEAD PROTECTION</span>
  </div>

  <div class="ppe-item" style="left:65px; top:320px;">
    <svg class="ppe-icon" viewBox="0 0 120 120" aria-hidden="true">
      <circle cx="60" cy="60" r="57" fill="none" stroke="var(--accent)" stroke-width="3"/>
      <path d="M30 70 V58 A30 30 0 0 1 90 58 V70" fill="none" stroke="var(--accent)" stroke-width="7"/>
      <rect x="22" y="64" width="16" height="28" rx="5" fill="var(--accent)"/>
      <rect x="82" y="64" width="16" height="28" rx="5" fill="var(--accent)"/>
    </svg>
    <span class="ppe-label">HEARING PROTECTION</span>
  </div>

  <div class="ppe-item" style="left:65px; top:615px;">
    <svg class="ppe-icon" viewBox="0 0 120 120" aria-hidden="true">
      <circle cx="60" cy="60" r="57" fill="none" stroke="var(--accent)" stroke-width="3"/>
      <path d="M40 18 H80 L86 96 H68 L60 44 L52 96 H34 Z" fill="var(--accent)"/>
    </svg>
    <span class="ppe-label">CHAPS PANTS</span>
  </div>

  <div class="ppe-item" style="left:65px; top:840px;">
    <svg class="ppe-icon" viewBox="0 0 120 120" aria-hidden="true">
      <circle cx="60" cy="60" r="57" fill="none" stroke="var(--accent)" stroke-width="3"/>
      <path d="M34 30 H60 V62 L92 74 Q96 78 94 84 H28 V70 Q34 60 34 50 Z" fill="var(--accent)"/>
      <rect x="28" y="86" width="66" height="6" fill="var(--accent)"/>
    </svg>
    <span class="ppe-label">FOOT PROTECTION</span>
  </div>

  <!-- Right column -->
  <div class="ppe-item" style="left:749px; top:48px;">
    <svg class="ppe-icon" viewBox="0 0 120 120" aria-hidden="true">
      <circle cx="60" cy="60" r="57" fill="none" stroke="var(--accent)" stroke-width="3"/>
      <path d="M20 48 Q60 40 100 48 L96 70 Q80 76 68 70 L60 62 L52 70 Q40 76 24 70 Z" fill="none" stroke="var(--accent)" stroke-width="4" stroke-linejoin="round"/>
    </svg>
    <span class="ppe-label">EYE PROTECTION</span>
  </div>

  <div class="ppe-item" style="left:775px; top:408px;">
    <svg class="ppe-icon" viewBox="0 0 120 120" aria-hidden="true" style="margin-left:94px;">
      <circle cx="60" cy="60" r="57" fill="none" stroke="var(--accent)" stroke-width="3"/>
      <path d="M36 22 H48 L60 48 L72 22 H84 L94 40 V94 H26 V40 Z" fill="var(--accent)"/>
      <rect x="26" y="62" width="68" height="6" fill="#fff"/>
      <rect x="26" y="76" width="68" height="6" fill="#fff"/>
      <rect x="58" y="48" width="4" height="46" fill="#fff"/>
    </svg>
    <span class="ppe-label">HIGH VISIBILITY HAT, VEST</span>
  </div>

  <div class="ppe-item" style="left:749px; top:598px;">
    <svg class="ppe-icon" viewBox="0 0 120 120" aria-hidden="true">
      <circle cx="60" cy="60" r="57" fill="none" stroke="var(--accent)" stroke-width="3"/>
      <path d="M22 48 L34 38 L56 70 L50 92 Z" fill="var(--accent)"/>
      <path d="M98 40 L86 28 L62 66 L66 90 Z" fill="var(--accent)"/>
    </svg>
    <span class="ppe-label">HAND PROTECTION</span>
  </div>

  <div class="ppe-item" style="left:749px; top:790px;">
    <svg class="ppe-icon" viewBox="0 0 120 120" aria-hidden="true">
      <circle cx="60" cy="60" r="57" fill="none" stroke="var(--accent)" stroke-width="3"/>
      <rect x="40" y="20" width="40" height="44" fill="none" stroke="var(--accent)" stroke-width="6"/>
      <path d="M40 20 L80 64 M80 20 L40 64" stroke="var(--accent)" stroke-width="5"/>
      <rect x="36" y="66" width="48" height="10" fill="var(--accent)"/>
      <path d="M40 80 H80 V90 L60 98 L40 90 Z" fill="none" stroke="var(--accent)" stroke-width="5"/>
    </svg>
    <span class="ppe-label">HARNESS LANYARD</span>
  </div>

  <div class="brand">
    <span class="brand-name">Bluetide secure</span>
    <span class="brand-sub">Marlowe Construction Co.</span>
  </div>

</main>
</body>
</html>
```